Web Design Project - Investor Services

I would like a simple and elegant web design for my company "Corvalo Management". The company will provide services to Corporate and Institutional investors for their needs with local/foreign investment vehicles. The website will have four pages to start: home, about us, services, contact.
I already chose a logo, and I will attach the source file. The color that I will most probably use for the logo will be blue, and i also like grey with a white background. For the website I would like to see light colors, maybe light green or grey, with the logo either in blue, grey or white (depeding on the background).
Target Market(s)
Investment managers and tax/legal advisors from top firms. This is the reason why I want something simple and elegant.
Industry/Entity Type
Investment
Requirements
Nice to have
- I do not want many pictures in the website, but I might include a couple of pictures of Madrid and maybe a picture of myself in the about us page (still deciding). I will attach some pictures of Madrid that I like, but feel free to search for others - i have others but i am not able to attach all of them.

```html
<!DOCTYPE html>
<html lang="en">
<head>
<meta charset="utf-8">
<title>Corvalo Management</title>
<link href="https://fonts.googleapis.com/css2?family=Fira+Sans+Condensed:ital,wght@0,300;0,400;0,500;1,300&family=Noticia+Text:ital,wght@0,400;1,700&family=Raleway:wght@300&display=swap" rel="stylesheet">
<style>
  :root {
    --blue: #3d8fd1;
    --blue-light: #62aee8;
    --blue-dark: #3786c8;
    --ink: #4a4a4a;
    --ink-soft: #555;
    --panel: #f5f5f5;
    --border: #d9d9d9;
    --button: #474747;
    --rule: #e4e4e4;
    --white: #fff;
  }
  * { box-sizing: border-box; margin: 0; padding: 0; }
  html, body { width: 1200px; height: 918px; overflow: hidden; background: var(--white); }
  body { position: relative; font-family: "Fira Sans Condensed", sans-serif; color: var(--ink); }

  .hero {
    position: absolute; left: 155px; top: 0; width: 892px; height: 393px;
    border-radius: 0 0 26px 26px; overflow: hidden;
    background: linear-gradient(180deg, #5b88a6 0%, #8aa5b8 25%, #c9c3cc 55%, #c6a9b3 72%, #3a4a58 92%, #1e2730 100%);
    box-shadow: 0 2px 0 #e6e6e6, 0 3px 4px rgba(0,0,0,.15);
  }
  .brand {
    position: absolute; left: 88px; top: 14px;
    font-family: "Raleway", sans-serif; font-weight: 300; font-size: 38px;
    color: var(--white); letter-spacing: 1px;
  }

  .main-nav {
    position: absolute; left: 235px; top: 364px; width: 714px; height: 55px;
    background: linear-gradient(180deg, var(--blue-light), var(--blue-dark));
    border-radius: 2px;
  }
  .main-nav a {
    position: absolute; top: 17px; transform: translateX(-50%);
    font-weight: 500; font-size: 16px; color: var(--white); text-decoration: none;
  }
  .main-nav .sep { position: absolute; top: 20px; width: 1px; height: 16px; background: rgba(255,255,255,.6); }

  .welcome { position: absolute; left: 0; top: 451px; width: 1200px; text-align: center; }
  .welcome h1 {
    font-family: "Noticia Text", serif; font-style: italic; font-weight: 700;
    font-size: 24px; color: var(--ink-soft);
  }
  .welcome h1 span { color: var(--blue); }
  .welcome p {
    width: 840px; margin: 6px auto 0; font-style: italic; font-weight: 300;
    font-size: 16px; line-height: 23px; color: var(--ink);
  }

  .card {
    position: absolute; top: 587px; width: 277px; height: 186px;
    border: 1px solid var(--border); padding: 4px;
  }
  .card-inner { width: 100%; height: 100%; background: var(--panel); position: relative; padding: 18px 8px 0 20px; }
  .card h2 {
    display: flex; align-items: center; gap: 10px;
    font-family: "Noticia Text", serif; font-weight: 400; font-size: 23px; color: var(--blue);
  }
  .card h2 svg { width: 22px; height: 26px; fill: var(--ink-soft); }
  .card p { margin-top: 8px; font-weight: 300; font-size: 15px; line-height: 23px; color: var(--ink); letter-spacing: -0.1px; }
  .more {
    position: absolute; left: 17px; top: 133px; width: 55px; height: 29px;
    background: var(--button); color: var(--white); font-weight: 500; font-size: 16px;
    text-align: center; line-height: 29px; border-radius: 2px; text-decoration: none;
  }

  .site-footer { position: absolute; left: 136px; top: 805px; width: 911px; border-top: 1px solid var(--rule); text-align: center; }
  .footer-nav { margin-top: 17px; font-weight: 300; font-size: 14.5px; color: var(--ink); }
  .footer-nav a { color: var(--ink); text-decoration: none; margin: 0 6px; }
  .footer-nav a.current { color: var(--blue); }
  .copyright { margin-top: 3px; font-weight: 300; font-size: 14px; color: var(--ink); }
  .social { position: absolute; top: 73px; left: 437px; display: flex; gap: 6px; }
  .social span { width: 23px; height: 23px; border-radius: 3px; background: linear-gradient(180deg, #5d9ee0, #2f6db5); }
</style>
</head>
<body>
  <header class="hero" role="img" aria-label="Photograph of the Madrid business skyline with four tall towers against a cloudy sky">
    <div class="brand">Corvalo Management</div>
  </header>

  <nav class="main-nav">
    <a href="#" style="left:84px">Home</a>
    <span class="sep" style="left:166px"></span>
    <a href="#" style="left:248px">About Us</a>
    <span class="sep" style="left:341px"></span>
    <a href="#" style="left:419px">Services</a>
    <span class="sep" style="left:510px"></span>
    <a href="#" style="left:597px">Contact Us</a>
  </nav>

  <section class="welcome">
    <h1>Welcome to <span>Corvalo Management</span></h1>
    <p>The company provide services to Corporate and Institutional investors for their needs with local/foreign investment vehicles. The company provide services to Corporate and Institutional investors for their needs with local/foreign investment vehicles. The company provide services to Corporate and Institutional investors for their needs with local/foreign investment vehicles.</p>
  </section>

  <article class="card" style="left:160px">
    <div class="card-inner">
      <h2><svg viewBox="0 0 22 26"><path d="M3 0h16v9l-4 3h-8l-4-3z"/><circle cx="11" cy="18" r="7"/><path d="M11 14l1.3 2.7 2.9.4-2.1 2 .5 2.9-2.6-1.4-2.6 1.4.5-2.9-2.1-2 2.9-.4z" fill="#f5f5f5"/></svg>About Us</h2>
      <p>The company will provide services tInvestment managers and tax/legal advisors from top firms.</p>
      <a class="more" href="#">More</a>
    </div>
  </article>

  <article class="card" style="left:465px">
    <div class="card-inner">
      <h2><svg viewBox="0 0 26 26" style="width:26px"><path d="M8 8V5a5 5 0 0 1 10 0v3h-2V5a3 3 0 0 0-6 0v3z"/><rect x="1" y="8" width="24" height="17" rx="2"/></svg>Services</h2>
      <p>The company will provide services tInvestment managers and tax/legal advisors from top firms.</p>
      <a class="more" href="#">More</a>
    </div>
  </article>

  <article class="card" style="left:768px">
    <div class="card-inner">
      <h2><svg viewBox="0 0 26 26" style="width:26px"><path d="M13 1L1 10v15h24V10z"/><path d="M6 11h14v5l-7 4-7-4z" fill="#f5f5f5"/></svg>Contact Us</h2>
      <p>Write here something about your company address and phone no, email id etc for your esteemed clients.</p>
      <a class="more" href="#" style="top:135px">More</a>
    </div>
  </article>

  <footer class="site-footer">
    <div class="footer-nav"><a class="current" href="#">Home</a> | <a href="#">About Us</a> | <a href="#">Services</a> | <a href="#">Contact Us</a></div>
    <div class="copyright">Copyright@2013, Corvalo Management</div>
    <div class="social"><span></span><span></span></div>
  </footer>
</body>
</html>
```